Whitepaper on Cyber Security for Community Banks & Credit Unions

I need to turn a basic whitepaper into a nice eBook we can use with a landing page on our website. We have several eBooks we publish so this is a test to see if we can being to use DesignCrowd to help with those projects. We are not done with final editing of the words so whatever is produced need to be editable on our side--however basic framework of the doc is complete (words might change in the paragraphs)

Target Market(s)

Bank and Credit Union Executive Managment

Industry/Entity Type

Security

Font styles to use
Serif
Sans Serif

Requirements
Must have
• works with our website design https://brimlofter.com

```html
<!DOCTYPE html>
<html lang="en">
<head>
<meta charset="utf-8">
<title>Preparing for a Data Breach – Page 4</title>
<link href="https://fonts.googleapis.com/css2?family=Source+Sans+3:ital,wght@0,400;0,600;0,700;1,400&family=Open+Sans:wght@700;800&display=swap" rel="stylesheet">
<style>
  :root {
    --ink: #1e1e1e;
    --muted: #8a8a8a;
    --brand-navy: #0d2b57;
    --brand-blue: #1c5fa8;
    --panel-top: #1a5aa0;
    --panel-mid: #3f7fbd;
    --panel-light: #c9dcee;
    --white: #ffffff;
  }
  * { margin: 0; padding: 0; box-sizing: border-box; }
  html, body { width: 849px; height: 1200px; overflow: hidden; background: var(--white); }
  body { font-family: "Source Sans 3", "Myriad Pro", sans-serif; color: var(--ink); }
  .page { position: relative; width: 849px; height: 1200px; overflow: hidden; }

  .running-head { position: absolute; left: 40px; top: 48px; font-size: 14px; color: var(--muted); }

  .brand { position: absolute; right: 42px; top: 52px; display: flex; align-items: center; gap: 8px; }
  .brand-mark { width: 26px; height: 26px; background: var(--brand-navy); }
  .brand-name { font-family: "Source Sans 3", sans-serif; font-weight: 700; font-size: 31px; color: var(--brand-blue); letter-spacing: -0.3px; line-height: 1; }

  .body-column { position: absolute; left: 40px; top: 110px; width: 413px; font-size: 14px; line-height: 17.2px; text-align: justify; }
  .body-column strong { font-weight: 700; }
  .bullets { list-style: none; margin: 3px 0 2px 0; text-align: left; }
  .bullets li { position: relative; padding-left: 36px; padding-right: 6px; margin-bottom: 5.6px; }
  .bullets li:last-child { margin-bottom: 2px; }
  .bullets li::before { content: "o"; position: absolute; left: 18px; top: 0; }
  .section-title { font-weight: 700; }
  .section-title + p { margin-top: 7px; }

  .callout-panel {
    position: absolute; left: 483px; top: 115px; width: 324px; height: 1025px;
    background: linear-gradient(180deg, var(--panel-top) 0%, var(--panel-top) 40%, var(--panel-mid) 62%, var(--panel-light) 100%);
  }
  .callout-text {
    position: absolute; left: 22px; top: 38px; width: 272px;
    font-family: "Open Sans", sans-serif; font-weight: 700; font-size: 18.4px; line-height: 24.1px;
    color: var(--white); text-transform: uppercase; letter-spacing: -0.2px;
  }
  .keyboard-photo {
    position: absolute; left: 0; top: 470px; width: 324px; height: 555px;
    background: radial-gradient(ellipse at 60% 55%, #eef4fa 0%, #b8d0e8 45%, rgba(63,127,189,0) 80%);
  }

  .folio { position: absolute; left: 398px; top: 1152px; font-size: 14px; font-style: italic; color: var(--muted); }
</style>
</head>
<body>
<div class="page">
  <div class="running-head">Preparing for a Data Breach</div>

  <div class="brand">
    <span class="brand-mark"></span>
    <span class="brand-name">Brimlofter</span>
  </div>

  <div class="body-column">
    <p><strong>2. Information Systems.</strong> The Safeguards Rule requires a financial institution to assess its information systems, including network and software design, as well as information processing, storage, transmission, and disposal. A financial institution’s written information security plan should include both technology concerns and the physical storage and destruction of nonpublic personal information. For example:</p>
    <ul class="bullets">
      <li>Know where sensitive customer information is stored and stored securely;</li>
      <li>Ensure that the computer or server is accessible only by using a “strong” password and is kept in a physically secure area;</li>
      <li>Maintain secure backup records and keep archived data secure by storing it off-line and in a physically secure area;</li>
      <li>Take affirmative steps to secure transmission of customer information;</li>
      <li>Encrypt customer data if it is necessary for you to transmit such information by email or Internet;</li>
      <li>If you collect information online directly from customers, secure the data transmission automatically;</li>
      <li>Dispose of customer information consistent with the FTC’s Disposal Rule.</li>
    </ul>
    <p><strong>3. Plan for System Attacks.</strong> The Safeguards Rule requires a financial institution to detect, prevent, and respond to attacks, intrusions, or other system failures. A financial institution must remain constantly vigilant, and employ the latest security measures and technology in order to adequately protect its network. The FTC Guidance report suggests that financial institutions:</p>
    <ul class="bullets">
      <li>Monitor the websites of software vendors and relevant industry publications for news about emerging threats and available defenses;</li>
      <li>Maintain up-to-date and appropriate programs and controls to prevent unauthorized access to customer information;</li>
      <li>Use appropriate oversight or audit procedures to detect the improper disclosure or theft of customer information;</li>
      <li>Take affirmative steps to preserve the security, confidentiality, and integrity of customer information and consider notifying consumers, law enforcement, and credit bureaus in the event of a security breach;</li>
      <li>Oversee service providers by ensuring that they are able to take appropriate security precautions and in fact do so;</li>
      <li>Update the security program as necessary in response to frequent monitoring and material changes in the business.</li>
    </ul>
    <p class="section-title">C. Implementing and Maintaining the Information Security Program.</p>
    <p>The Safeguards Rule requires an institution to design and implement information safeguards to control the risks identified and regularly test and monitor the effectiveness of the information security program’s key controls, systems, and procedures. This duty also includes overseeing third-party service providers by taking reasonable steps to ensure that the service provider is capable of maintaining appropriate safeguards and requiring the service providers to contractually agree to implement and maintain such controls. The Safeguards Rule requires a financial institution to evaluate and adjust its information security program in response to its system test results or in response to any changes in its operations or business circumstances.</p>
  </div>

  <aside class="callout-panel">
    <p class="callout-text">An important factor for institutions to consider is the potential discoverability of risk assessments. Talk to an experienced cyber security attorney about avoiding potential discovery issues and have any risk assessments covered by the attorney-client or the attorney work-product privilege. The rules regarding these privileges are state specific.</p>
    <div class="keyboard-photo" role="img" aria-label="Close-up photo of a light keyboard with a key marked Security and a padlock symbol"></div>
  </aside>

  <div class="folio">Page #4</div>
</div>
</body>
</html>
```